Project Planning & Communication Process

Need a PowerPoint slide that illustrates our project planning and communication cycle. Our company has key meetings, and key communication vehicles (like emails and follow up tools) that we use to ensure our frontline staff are prepared to execute the new project successfully. This document needs to call out how the different components, like the meetings and emails, work together (like a flow chart), so someone who needs to use this process will understand what they should do. The slide needs to be simple yet comprehensive enough to guide someone through the details. I don't want it overwhelming. The primary focus is the process, not the details.

Use the color pallette included within the slide (shades of blue and gray, and black). This is for an insurance company (www.marrowpine.com). Use this as a reference for the look and feel.

I have attached a sample slide of the flow chart process.

Click here if you cannot access the file. https://www.stashloft.com/s/qx7rmt2pbn9wkaz/Communcation_Methods_V1.pptx

If you are not able to see the uploaded slide.  Please send me your email address and I will send the slide to you directly. 

ISince I'm not able to upload the reference ppt file, 've uploaded the slide at StashLoft.  Please click here to access.
https://www.stashloft.com/s/qx7rmt2pbn9wkaz/Communcation_Methods_V1.pptx

Reason: extending one more day for designers to make last minute updates.

Target Market(s)

Vice Presidents and project managers/business partners within the organization.

Industry/Entity Type

Communication

Font styles to use
Sans Serif

Colors
3176b5

Requirements
Must have
• 1 page, color pallette assigned, be simple yet comprehensive. the focus needs to be on the process, not on the details.
Nice to have
• Doesn't have to follow the example I provided. Please feel free to approach from different ways.

```html
<!DOCTYPE html>
<html lang="en">
<head>
<meta charset="utf-8">
<title>Project Alignment &amp; Project Communication Process</title>
<link href="https://fonts.googleapis.com/css2?family=Open+Sans:wght@300;400;600&display=swap" rel="stylesheet">
<style>
  :root {
    --navy: #1f6391;
    --deep: #1d5b86;
    --blue: #158ad0;
    --teal: #17b2c9;
    --pale: #b5e7f2;
    --pale-text: #2b82bd;
    --grey: #bfbfbf;
    --grey-light: #d9d9d9;
    --canvas: #f2f2f2;
    --ink: #222222;
    --white: #ffffff;
  }
  * { box-sizing: border-box; margin: 0; padding: 0; }
  html, body { width: 1200px; height: 900px; overflow: hidden; }
  body {
    position: relative;
    background: var(--canvas);
    font-family: "Open Sans", Arial, sans-serif;
    color: var(--ink);
  }
  .title-bar {
    position: absolute; left: 0; top: 0; width: 1200px; height: 70px;
    background: var(--navy);
    display: flex; align-items: center;
  }
  .title-bar svg { margin-left: 48px; }
  .title-bar h1 {
    margin-left: 28px;
    font-weight: 300; font-size: 33px; letter-spacing: 0.5px;
    color: var(--white);
  }
  .phase {
    position: absolute; top: 90px; height: 45px;
    background: var(--grey-light); color: var(--navy);
    display: flex; align-items: center; justify-content: center; text-align: center;
    font-size: 20px; font-weight: 400; letter-spacing: 0.3px;
  }
  .phase.small { font-size: 14px; line-height: 1.25; letter-spacing: 0.8px; }
  .clock { position: absolute; top: 148px; }
  .timing {
    position: absolute; top: 181px; height: 26px;
    background: var(--grey-light); color: var(--ink);
    font-size: 11px; display: flex; align-items: center; justify-content: center;
  }
  .step {
    position: absolute; top: 210px; height: 187px;
    display: flex; flex-direction: column; align-items: center; justify-content: center;
    text-align: center; color: var(--white);
    padding: 0 12px 0 16px;
    clip-path: polygon(0 0, calc(100% - 12px) 0, 100% 50%, calc(100% - 12px) 100%, 0 100%, 12px 50%);
  }
  .step.first { clip-path: polygon(0 0, 100% 0, 100% 100%, 0 100%); padding: 0 16px 0 8px; }
  .step.last { clip-path: polygon(0 0, 100% 0, 100% 100%, 0 100%, 12px 50%); }
  .step .name { font-size: 14px; line-height: 1.3; }
  .step .note { font-size: 9.5px; line-height: 1.35; margin-top: 12px; }
  .step.grey { background: var(--grey); color: var(--navy); }
  .step.grey.mid { color: var(--white); }
  .step.blue { background: var(--blue); }
  .step.deep { background: var(--deep); }
  .outcome {
    position: absolute; top: 397px; height: 97px;
    background: var(--teal); color: var(--white);
    font-size: 12px; font-weight: 600; line-height: 1.4; text-align: center;
    padding: 12px 8px 0;
  }
  .detail {
    position: absolute; top: 498px; height: 202px;
    background: var(--pale); color: var(--pale-text);
    font-size: 11.5px; line-height: 1.45; text-align: center;
    padding: 10px 10px 0;
  }
  .detail.short { height: 199px; }
  .legend { position: absolute; top: 742px; height: 66px;
    display: flex; flex-direction: column; align-items: center; justify-content: center; gap: 6px;
    font-size: 14px; color: var(--white); }
  .legend.meetings { background: var(--blue); }
  .legend.emails { background: var(--deep); }
  .legend.purpose { background: var(--teal); }
  .legend.overview { background: var(--pale); color: var(--pale-text); }
  .brand {
    position: absolute; right: 40px; top: 854px;
    display: flex; align-items: center; gap: 8px;
    font-size: 20px; font-weight: 600; color: var(--navy);
  }
  .brand .mark { width: 16px; height: 16px; background: var(--navy); }
  .foot { position: absolute; top: 887px; height: 13px; }
</style>
</head>
<body>
  <header class="title-bar">
    <svg width="30" height="40" viewBox="0 0 30 40"><path d="M5 3 L22 20 L5 37" fill="none" stroke="#fff" stroke-width="7"/></svg>
    <h1>PROJECT ALIGNMENT &amp; PROJECT COMMUNICATION PROCESS</h1>
  </header>

  <div class="phase" style="left:20px;width:691px">PLANNING &amp; DESIGN PHASE</div>
  <div class="phase" style="left:717px;width:340px">PREPARE PHASE</div>
  <div class="phase small" style="left:1064px;width:114px">FOLLOW UP<br>&amp; EVALUATE</div>

  <svg class="clock" style="left:176px" width="28" height="28" viewBox="0 0 28 28"><circle cx="14" cy="14" r="11.5" fill="#fff" stroke="#444" stroke-width="2"/><path d="M14 7v7l-5 3" fill="none" stroke="#444" stroke-width="2"/><rect x="12" y="0" width="4" height="3" fill="#444"/></svg>
  <svg class="clock" style="left:523px" width="28" height="28" viewBox="0 0 28 28"><circle cx="14" cy="14" r="11.5" fill="#fff" stroke="#444" stroke-width="2"/><path d="M14 7v7l-5 3" fill="none" stroke="#444" stroke-width="2"/><rect x="12" y="0" width="4" height="3" fill="#444"/></svg>
  <svg class="clock" style="left:757px" width="28" height="28" viewBox="0 0 28 28"><circle cx="14" cy="14" r="11.5" fill="#fff" stroke="#444" stroke-width="2"/><path d="M14 7v7l-5 3" fill="none" stroke="#444" stroke-width="2"/><rect x="12" y="0" width="4" height="3" fill="#444"/></svg>
  <svg class="clock" style="left:870px" width="28" height="28" viewBox="0 0 28 28"><circle cx="14" cy="14" r="11.5" fill="#fff" stroke="#444" stroke-width="2"/><path d="M14 7v7l-5 3" fill="none" stroke="#444" stroke-width="2"/><rect x="12" y="0" width="4" height="3" fill="#444"/></svg>

  <div class="timing" style="left:137px;width:113px">3 + Months out</div>
  <div class="timing" style="left:484px;width:112px">2+ months out</div>
  <div class="timing" style="left:715px;width:112px">1 month out</div>
  <div class="timing" style="left:831px;width:113px">1 Week out</div>

  <div class="step grey first" style="left:24px;width:123px"><p class="name">New Project Identified</p></div>
  <div class="step blue" style="left:137px;width:125px"><p class="name">Governance Meeting</p></div>
  <div class="step grey mid" style="left:252px;width:124px"><p class="name">Separate Project Meetings as needed</p></div>
  <div class="step blue" style="left:367px;width:124px"><p class="name">Governance Meeting</p></div>
  <div class="step blue" style="left:482px;width:126px"><p class="name">Weekly Center Leader Meeting</p></div>
  <div class="step blue" style="left:599px;width:123px"><p class="name">Field Advisory Panel</p><p class="note">Purpose:<br>Collect Feedback<br><br>When:<br>As needed</p></div>
  <div class="step blue" style="left:715px;width:124px"><p class="name">Weekly Center Leader Meeting</p><p class="note">Purpose:<br>Center Planning and Specific execution details<br><br>When:<br>1 month out</p></div>
  <div class="step deep" style="left:831px;width:125px"><p class="name">Monday Memo</p><p class="note">1 week out</p></div>
  <div class="step deep" style="left:947px;width:124px"><p class="name">Daily Digest</p><p class="note">Just in Time Notice/Follow up for execution</p></div>
  <div class="step deep last" style="left:1062px;width:116px"><p class="name">Follow Up Guide</p><p class="note">Post Launch</p></div>

  <div class="outcome" style="left:137px;width:113px">Go/No Go Decision</div>
  <div class="outcome" style="left:367px;width:112px">Report out on Milestone status and Key Decision Points</div>
  <div class="outcome" style="left:482px;width:114px">Introduce Project &amp; gather Center Leader Feedback</div>
  <div class="outcome" style="left:599px;width:111px">Collect Center Staff Feedback</div>
  <div class="outcome" style="left:715px;width:112px">Provide Center Leaders with Implementation Details</div>

  <div class="detail short" style="left:137px;width:113px">Project Owner presents a one pager to Sr Leadership. Business Value and Capacity drive the Go/No Go Decision.</div>
  <div class="detail" style="left:367px;width:112px">Project Owner reports milestone progress, flags risks and brings key decisions to Sr Leadership for approval.</div>
  <div class="detail" style="left:482px;width:114px">Project Owner introduces scope and timeline to Center Leaders and captures their questions and early feedback.</div>
  <div class="detail" style="left:599px;width:111px">Frontline staff review the plan as needed and share feedback on workflow, tools and readiness.</div>
  <div class="detail" style="left:715px;width:112px">Center Leaders receive final plans, roles and execution details to prepare their teams for launch.</div>

  <div class="legend meetings" style="left:354px;width:103px">
    <svg width="36" height="24" viewBox="0 0 36 24" fill="#fff"><circle cx="9" cy="6" r="4"/><circle cx="18" cy="5" r="4.5"/><circle cx="27" cy="6" r="4"/><path d="M2 22c0-6 3-9 7-9s7 3 7 9z"/><path d="M20 22c0-6 3-9 7-9s7 3 7 9z"/><path d="M10 23c0-7 4-10 8-10s8 3 8 10z"/></svg>
    <span>Meetings</span>
  </div>
  <div class="legend emails" style="left:471px;width:111px">
    <svg width="30" height="22" viewBox="0 0 30 22"><rect x="1" y="1" width="28" height="20" fill="#fff"/><path d="M1 1 L15 13 L29 1" fill="none" stroke="#1d5b86" stroke-width="2"/></svg>
    <span>Emails</span>
  </div>
  <div class="legend purpose" style="left:602px;width:104px">
    <svg width="26" height="26" viewBox="0 0 26 26"><rect x="3" y="3" width="16" height="21" fill="none" stroke="#fff" stroke-width="2.2"/><path d="M10 17 L22 3 L25 6 L13 20 L9 21 Z" fill="#fff"/></svg>
    <span>Purpose</span>
  </div>
  <div class="legend overview" style="left:721px;width:110px">
    <svg width="34" height="22" viewBox="0 0 34 22"><path d="M1 11 Q17 -6 33 11 Q17 28 1 11 Z" fill="none" stroke="#2b82bd" stroke-width="2.4"/><circle cx="17" cy="11" r="5" fill="#2b82bd"/></svg>
    <span>Overview</span>
  </div>

  <div class="brand"><span>Marrow Pine</span><span class="mark"></span></div>

  <div class="foot" style="left:0;width:393px;background:var(--blue)"></div>
  <div class="foot" style="left:397px;width:424px;background:var(--deep)"></div>
  <div class="foot" style="left:826px;width:374px;background:var(--teal)"></div>
</body>
</html>
```